Business Card Design Project

My company/business is called K-LUX Restaurant Marketing.
K-LUX = Kindle Loyalty Using eXperience (which is our tagline if you will)

Industry/Entity Type

Business

Contact Information for Business Card

The Image below is the way I want my cards to look.

A 1-sided design on clear plastic stock would be awesome
.
I don't want the "Velcor 3G" data design. Instead, replace that with "K-LUX". That way people know their business is running from K-LUX "network" (my company is called K-LUX Restaurant Marketing).

My name is Tomas Varga, and my title is "Founder & C.E.O". I want it written exactly like I just wrote it please. so that can replace the part of the image where it says "Corporate Director".

instead of the address below the Name & Title, I would like it to say
"K-LUX Restaurant Marketing" and in smaller letters below, my tagline: "Kindle Loyalty Using eXperience".

I don't need the Skype handle on there. That should free up space for my business name and tagline from above. I want the rest to stay the same, but change the information.
- Phone Number: +1 (831) 555-0148
- Email: tomas.varga1@postvale.com
- Web Address: www.kluxrestaurantmarketing.com

Finally, I want the symbols at the bottom to change. They can stay black and white, and be simple as they currently are in the picture, but I want to replace the current images with the social media symbols for Pagebloom, Picwell, Quillet, VexMo, and Streamora.

```html
<!DOCTYPE html>
<html lang="en">
<head>
<meta charset="utf-8">
<title>K-LUX Restaurant Marketing — Business Card</title>
<link rel="stylesheet" href="https://fonts.googleapis.com/css2?family=Montserrat:wght@400;600;700;800&family=Libre+Baskerville:wght@700&display=swap">
<style>
  :root {
    --backdrop: #6f7072;
    --card-top: #b9b8b7;
    --card-bottom: #a8a7a6;
    --ink: #111111;
    --ink-soft: #222222;
    --screen-black: #050505;
    --screen-sheen: #262626;
    --accent-red: #e0313d;
    --icon-grey: #8a8a8a;
  }
  * { margin: 0; padding: 0; box-sizing: border-box; }
  html, body { width: 1200px; height: 1000px; overflow: hidden; }
  body {
    background: var(--backdrop);
    font-family: "Montserrat", Arial, sans-serif;
    color: var(--ink);
    position: relative;
  }
  .card {
    position: absolute;
    left: 333px; top: 50px;
    width: 534px; height: 900px;
    border-radius: 30px;
    background: linear-gradient(180deg, var(--card-top), var(--card-bottom));
  }
  .earpiece-band, .home-band {
    position: absolute;
    left: 52px; width: 430px;
    border-radius: 14px;
    background: linear-gradient(160deg, var(--screen-sheen) 0%, var(--screen-black) 35%, var(--screen-black) 100%);
  }
  .earpiece-band { top: 35px; height: 115px; }
  .home-band { top: 755px; height: 105px; display: flex; align-items: center; justify-content: center; }
  .camera {
    position: absolute; left: 70px; top: 50px;
    width: 18px; height: 18px; border-radius: 50%;
    background: radial-gradient(circle at 40% 40%, #4a5a78, #0b0d14 70%);
  }
  .speaker {
    position: absolute; left: 150px; top: 42px;
    width: 120px; height: 30px; border-radius: 15px;
    background: #2a2a2a;
  }
  .home-brand {
    font-weight: 700; font-size: 22px; letter-spacing: 2px;
    color: var(--icon-grey);
  }
  .status-bar {
    position: absolute; left: 52px; top: 163px; width: 430px;
    display: flex; align-items: center; justify-content: space-between;
    font-size: 15px; font-weight: 600;
  }
  .status-left { display: flex; align-items: center; gap: 8px; }
  .status-right { display: flex; align-items: center; gap: 6px; }
  .identity { position: absolute; left: 0; top: 218px; width: 100%; text-align: center; }
  .person-name { font-size: 48px; font-weight: 800; line-height: 1; letter-spacing: -0.5px; }
  .person-title { font-size: 19px; font-weight: 400; margin-top: 2px; }
  .brand-block { position: absolute; left: 0; top: 312px; width: 100%; display: flex; flex-direction: column; align-items: center; }
  .brand-name { font-size: 46px; font-weight: 800; line-height: 1; }
  .brand-service {
    font-size: 22px; font-weight: 700; text-transform: uppercase; line-height: 1.1;
    border-top: 2px solid var(--ink); border-bottom: 2px solid var(--ink);
    padding: 1px 2px; margin-top: 3px;
  }
  .brand-tagline {
    font-family: "Libre Baskerville", Georgia, serif;
    font-size: 12px; font-weight: 700; text-transform: uppercase; margin-top: 4px;
  }
  .contacts { position: absolute; left: 64px; top: 444px; list-style: none; }
  .contact { display: flex; align-items: center; gap: 23px; height: 48px; margin-bottom: 13px; }
  .contact-badge {
    width: 48px; height: 48px; border-radius: 50%;
    background: var(--accent-red);
    display: flex; align-items: center; justify-content: center; flex-shrink: 0;
  }
  .contact-value { font-size: 19px; font-weight: 700; line-height: 1.1; }
  .contact-label { font-size: 19px; font-weight: 400; line-height: 1.1; }
  .socials {
    position: absolute; left: 52px; top: 690px; width: 430px;
    display: flex; justify-content: space-between; list-style: none;
  }
  .social { width: 86px; display: flex; flex-direction: column; align-items: center; gap: 4px; }
  .social-square { width: 34px; height: 34px; border: 3px solid var(--ink); border-radius: 6px; }
  .social-name { font-size: 12px; font-weight: 700; }
</style>
</head>
<body>
  <article class="card" aria-label="Business card for Tomas Varga, K-LUX Restaurant Marketing">
    <div class="earpiece-band">
      <span class="camera"></span>
      <span class="speaker"></span>
    </div>

    <div class="status-bar">
      <div class="status-left">
        <svg width="22" height="12" viewBox="0 0 22 12" aria-hidden="true">
          <rect x="0" y="8" width="3" height="4" fill="#111"/>
          <rect x="5" y="6" width="3" height="6" fill="#111"/>
          <rect x="10" y="4" width="3" height="8" fill="#111"/>
          <rect x="15" y="2" width="3" height="10" fill="#111"/>
          <rect x="19" y="0" width="3" height="12" fill="#111"/>
        </svg>
        <span class="carrier">K-LUX</span>
        <svg width="22" height="16" viewBox="0 0 22 16" aria-hidden="true">
          <path d="M1 6 A14 14 0 0 1 21 6" fill="none" stroke="#111" stroke-width="2.4"/>
          <path d="M5 10 A8 8 0 0 1 17 10" fill="none" stroke="#111" stroke-width="2.4"/>
          <circle cx="11" cy="14" r="2" fill="#111"/>
        </svg>
      </div>
      <span class="clock">12:34 PM</span>
      <div class="status-right">
        <span>100%</span>
        <svg width="26" height="12" viewBox="0 0 26 12" aria-hidden="true">
          <rect x="1" y="1" width="21" height="10" rx="1.5" fill="none" stroke="#111" stroke-width="1.6"/>
          <rect x="3" y="3" width="17" height="6" fill="#111"/>
          <rect x="23" y="4" width="2.5" height="4" fill="#111"/>
        </svg>
      </div>
    </div>

    <header class="identity">
      <h1 class="person-name">Tomas Varga</h1>
      <p class="person-title">Founder &amp; C.E.O</p>
    </header>

    <div class="brand-block">
      <p class="brand-name">K-LUX</p>
      <p class="brand-service">Restaurant Marketing</p>
      <p class="brand-tagline">Kindle Loyalty Using eXperience</p>
    </div>

    <ul class="contacts">
      <li class="contact">
        <span class="contact-badge">
          <svg width="26" height="26" viewBox="0 0 24 24" aria-hidden="true">
            <path d="M6.6 10.8a15 15 0 0 0 6.6 6.6l2.2-2.2a1 1 0 0 1 1-.25 11.4 11.4 0 0 0 3.6.57 1 1 0 0 1 1 1V20a1 1 0 0 1-1 1A17 17 0 0 1 3 4a1 1 0 0 1 1-1h3.5a1 1 0 0 1 1 1c0 1.25.2 2.45.57 3.6a1 1 0 0 1-.25 1z" fill="#fff"/>
          </svg>
        </span>
        <div><p class="contact-value">+1 (831) 555-0148</p><p class="contact-label">Phone number</p></div>
      </li>
      <li class="contact">
        <span class="contact-badge">
          <svg width="26" height="20" viewBox="0 0 26 20" aria-hidden="true">
            <rect x="1" y="1" width="24" height="18" rx="2" fill="#fff"/>
            <path d="M2 2 L13 11 L24 2" fill="none" stroke="#e0313d" stroke-width="2"/>
          </svg>
        </span>
        <div><p class="contact-value">tomas.varga1@postvale.com</p><p class="contact-label">Email address</p></div>
      </li>
      <li class="contact">
        <span class="contact-badge">
          <svg width="26" height="26" viewBox="0 0 26 26" aria-hidden="true">
            <circle cx="13" cy="13" r="10.5" fill="none" stroke="#fff" stroke-width="2"/>
            <ellipse cx="13" cy="13" rx="4.5" ry="10.5" fill="none" stroke="#fff" stroke-width="2"/>
            <line x1="2.5" y1="13" x2="23.5" y2="13" stroke="#fff" stroke-width="2"/>
          </svg>
        </span>
        <div><p class="contact-value">www.kluxrestaurantmarketing.com</p><p class="contact-label">Web address</p></div>
      </li>
    </ul>

    <ul class="socials">
      <li class="social"><span class="social-square"></span><span class="social-name">Pagebloom</span></li>
      <li class="social"><span class="social-square"></span><span class="social-name">Picwell</span></li>
      <li class="social"><span class="social-square"></span><span class="social-name">Quillet</span></li>
      <li class="social"><span class="social-square"></span><span class="social-name">VexMo</span></li>
      <li class="social"><span class="social-square"></span><span class="social-name">Streamora</span></li>
    </ul>

    <div class="home-band">
      <span class="home-brand">K-LUX</span>
    </div>
  </article>
</body>
</html>
```